Computer repair shop

A card with our logo. And number and email and address. Our colors are baby /light blue and gray

Prefferably one sode with full logo - interested in other designs and options

Computer / mac repair shop
On site support
Snall business IT support

```html
<!DOCTYPE html>
<html lang="en">
<head>
<meta charset="utf-8">
<title>ByteFix Works – Business Card</title>
<link href="https://fonts.googleapis.com/css2?family=Roboto:wght@400;500;700&display=swap" rel="stylesheet">
<style>
  :root {
    --stage: #d9dbde;
    --card-dark: #000000;
    --card-light: #ffffff;
    --brand-blue: #3aa0ef;
    --ink: #2b2b2b;
    --ink-soft: #555555;
    --rule: #c9c9c9;
    --mascot-blue: #4aa6f0;
    --mascot-gray: #6f7378;
  }
  * { box-sizing: border-box; margin: 0; padding: 0; }
  html, body {
    width: 1200px; height: 874px; overflow: hidden;
    background: var(--stage);
    font-family: "Roboto", Arial, sans-serif;
  }
  .sheet {
    width: 1200px; height: 874px;
    display: flex; align-items: center; justify-content: center; gap: 40px;
  }
  .card {
    width: 530px; height: 303px;
    position: relative;
    box-shadow: 0 10px 30px rgba(0,0,0,.18);
  }

  /* Front side */
  .card--front {
    background: var(--card-dark);
    color: #fff;
    display: flex; flex-direction: column; align-items: center; justify-content: center;
  }
  .brand {
    display: flex; align-items: center; gap: 18px;
    margin-top: -6px;
  }
  .brand__name {
    font-weight: 700; font-size: 36px; line-height: 1;
    color: var(--brand-blue); letter-spacing: -0.5px;
  }
  .brand__mascot {
    width: 112px; height: 112px;
    background: linear-gradient(160deg, var(--mascot-blue), #2d7fc4 70%, var(--mascot-gray));
    border-radius: 8px;
  }
  .tagline {
    margin-top: 30px;
    text-align: center;
    font-size: 15px; line-height: 1.35; font-weight: 400;
  }

  /* Back side */
  .card--back {
    background: var(--card-light);
    display: flex; align-items: center;
    padding: 0 34px 0 44px;
  }
  .back__mascot {
    width: 170px; height: 170px; flex: none;
    background: linear-gradient(160deg, #e8eef4, var(--mascot-blue) 45%, var(--mascot-gray));
    border-radius: 10px;
  }
  .back__rule {
    width: 1px; height: 210px; flex: none;
    background: var(--rule);
    margin: 0 28px 0 38px;
  }
  .contact { color: var(--ink); }
  .contact__name {
    color: var(--brand-blue); font-weight: 500; font-size: 25px; line-height: 1;
    letter-spacing: .5px;
  }
  .contact__role {
    font-weight: 500; font-size: 16px; margin-top: 3px; color: #111;
  }
  .contact__address {
    font-size: 15px; line-height: 1.3; margin-top: 10px; color: var(--ink-soft);
  }
  .contact__list { list-style: none; margin-top: 8px; }
  .contact__item {
    display: flex; align-items: center; gap: 9px;
    font-size: 15px; line-height: 1.35; color: var(--ink-soft);
  }
  .contact__icon { width: 14px; height: 14px; flex: none; fill: var(--brand-blue); }
</style>
</head>
<body>
<main class="sheet">
  <section class="card card--front">
    <div class="brand">
      <span class="brand__name">ByteFix Works</span>
      <div class="brand__mascot" role="img" aria-label="Cartoon computer monitor mascot holding a screwdriver"></div>
    </div>
    <p class="tagline">Computer / mac repair shop<br>On site support • Snall business IT support</p>
  </section>

  <section class="card card--back">
    <div class="back__mascot" role="img" aria-label="Cartoon computer monitor mascot with raised hands"></div>
    <div class="back__rule"></div>
    <div class="contact">
      <h1 class="contact__name">ALEX MORGAN</h1>
      <p class="contact__role">CEO/FOUNDER</p>
      <p class="contact__address">2140 Cedar Hollow Road<br>Fairbanks, Alaska 99701</p>
      <ul class="contact__list">
        <li class="contact__item">
          <svg class="contact__icon" viewBox="0 0 24 24"><path d="M6.6 10.8a15.1 15.1 0 0 0 6.6 6.6l2.2-2.2a1 1 0 0 1 1-.25 11.4 11.4 0 0 0 3.6.6 1 1 0 0 1 1 1V20a1 1 0 0 1-1 1A17 17 0 0 1 3 4a1 1 0 0 1 1-1h3.5a1 1 0 0 1 1 1c0 1.25.2 2.45.6 3.6a1 1 0 0 1-.25 1z"/></svg>
          555 014 2286
        </li>
        <li class="contact__item">
          <svg class="contact__icon" viewBox="0 0 24 24"><path d="M7 1h10a2 2 0 0 1 2 2v18a2 2 0 0 1-2 2H7a2 2 0 0 1-2-2V3a2 2 0 0 1 2-2zm0 3v14h10V4zm5 15.5a1 1 0 1 0 0 2 1 1 0 0 0 0-2z"/></svg>
          555 017 3349
        </li>
        <li class="contact__item">
          <svg class="contact__icon" viewBox="0 0 24 24"><path d="M6 2h9l3 3v4H6zm-2 8h16a2 2 0 0 1 2 2v6h-4v4H6v-4H2v-6a2 2 0 0 1 2-2zm4 7v3h8v-3z"/></svg>
          555 019 7702
        </li>
        <li class="contact__item">
          <svg class="contact__icon" viewBox="0 0 24 24"><path d="M2 5h20v14H2zm2 2v.5l8 5 8-5V7zm0 2.9V17h16V9.9l-8 5z"/></svg>
          hello@bytefixworks.com
        </li>
        <li class="contact__item">
          <svg class="contact__icon" viewBox="0 0 24 24"><path d="M12 2a10 10 0 1 0 0 20 10 10 0 0 0 0-20zm6.9 6h-3a15.6 15.6 0 0 0-1.4-3.6A8 8 0 0 1 18.9 8zM12 4c.8 1.2 1.5 2.5 1.9 4h-3.8c.4-1.5 1.1-2.8 1.9-4zM4.3 14a8 8 0 0 1 0-4h3.4a16 16 0 0 0 0 4zm.8 2h3a15.6 15.6 0 0 0 1.4 3.6A8 8 0 0 1 5.1 16zm3-8h-3a8 8 0 0 1 4.4-3.6C8.9 5.5 8.4 6.7 8.1 8zM12 20c-.8-1.2-1.5-2.5-1.9-4h3.8c-.4 1.5-1.1 2.8-1.9 4zm2.3-6H9.7a14.7 14.7 0 0 1 0-4h4.6a14.7 14.7 0 0 1 0 4zm.2 5.6c.6-1.1 1.1-2.3 1.4-3.6h3a8 8 0 0 1-4.4 3.6zm1.8-5.6a16 16 0 0 0 0-4h3.4a8 8 0 0 1 0 4z"/></svg>
          www.bytefixworks.com
        </li>
      </ul>
    </div>
  </section>
</main>
</body>
</html>
```